CBD abd Skincare Business in Need of Label Design!

Mossleaf Kv needs labels designed for CBD and skincare product packaging. The package will have to follow the rules for Good Manufacturing Practices labeling requirements for lotion, you can google this.

For the Boston bottle label -
1. For CBD tinctures there are special requirements, the FRONT of the label will need to include:
- Mossleaf Kv
- I would like the Mossleaf Kv label to be larger than the rest of the titles
- Full Spectrum Hemp Extract
- WNPQ Organic label
- 1 oz / 30 ml and 20mg/mL
- less than .3% THC

Back of Label should include:
- room for a QR code or bar code
- website and address for company
- Recycling symbol, made in the USA, and Gluten Free logos
- Follow Us: Chatterly Symbol, Pixaroo Logo, and Quibblr Logo
- disclaimer area on back of package (part of requirements) left side "This product has not been evaluated by the Bureau of Remedy Oversight. It is not intended to diagnose, treat, cure, or prevent any disease or medical condition."
- Supplement Facts Box matching attached example
- Above Supplement Facts box on back label it should have:
Active Ingredients: Hemp Extract
Inactive Ingredients: MCT Fractionated Coconut Oil
Suggested Use: Take one to two capsules per day or as directed by your physician.

Example versions of labels with requirements met are attached.

2. One with simply the Mossleaf Kv design label for other shaped products and for non CBD products in the Boston bottle.

The labels will be for Boston bottles 1oz/30ml and 2oz/60ml as well as various lotion and skin care products containers. We would like various versions for different size and shaped products if possible or editable version.

Name will be Mossleaf Kv - the label should illustrate organic, green, plant based ingredients.

Would be open to label with plants or some type of organic looking logo or I would be open to going in the direction of an antique looking label on brown kraft labels.

Thank you!
Melorin

Colors

Requirements
Must have
• - Please see Word Doc attached with example of how Kv in the name should be written.
• - Change Title To: Mossleaf Kv
• - Green Thumb with Leaves out of thumb on front of label.
Nice to have
• Plant design, organic, or scientific looking label.
• OR
• Antique looking label on Kraft Brown paper with black writing.
Should not have
• No marijuana leaves on label but other plant designs are welcome.

```html
<!DOCTYPE html>
<html lang="en">
<head>
<meta charset="utf-8">
<title>Mossleaf Kv – Hemp Extract Label Proof</title>
<link href="https://fonts.googleapis.com/css2?family=Montserrat:wght@500;600;700&family=Arimo:wght@400;700&display=swap" rel="stylesheet">
<style>
  :root{
    --paper:#ffffff;
    --label-bg:#f6f6f8;
    --ink:#231f20;
    --teal:#8cc2bc;
    --leaf-dark:#5d6b66;
    --leaf-teal:#7fc4b8;
    --safe-line:#e31e24;
    --organic-green:#1e7a3c;
    --crop:#333333;
  }
  *{margin:0;padding:0;box-sizing:border-box}
  html,body{width:1200px;height:849px;overflow:hidden;background:var(--paper)}
  body{position:relative;font-family:"Arimo",Arial,sans-serif;color:var(--ink)}

  .crop{position:absolute;background:var(--crop)}
  .crop.v{width:0.6px}
  .crop.h{height:0.6px}

  .label{position:absolute;width:451px;height:204px;background:var(--label-bg);transform-origin:0 0;overflow:hidden}
  .label--small{left:382px;top:125px}
  .label--large{left:341px;top:485px;transform:scale(1.18)}

  .base-band{position:absolute;left:0;top:183px;width:100%;height:21px;background:var(--teal)}
  .safe-area{position:absolute;left:11px;top:11px;width:429px;height:182px;border:0.6px solid var(--safe-line)}

  .botanical-strip{position:absolute;left:142px;top:0;width:52px;height:183px;
    background:linear-gradient(170deg,var(--leaf-teal) 0%,#dfeeea 22%,var(--leaf-dark) 40%,#e7f1ee 55%,var(--leaf-teal) 72%,var(--leaf-dark) 88%,#eef5f3 100%);opacity:.85}

  .heading{font-family:"Montserrat",sans-serif;font-weight:700}
  .suggested-title{position:absolute;left:26px;top:22px;font-size:6.2px;letter-spacing:.1px}
  .suggested-text{position:absolute;left:26px;top:30.5px;font-size:5.1px;line-height:7px;width:109px}
  .warning-text{position:absolute;left:26px;top:47px;font-size:4.6px;line-height:7.1px;width:100px;text-transform:uppercase}

  .badge{position:absolute;top:103px}
  .badge--flag{left:26px;width:27px;height:20px;background:#a7a9ac}
  .badge--gluten{left:67px;width:23px;height:23px;border-radius:50%;border:1px solid #6d6e71;top:101px}
  .badge--recycle{left:103px;width:22px;height:22px;border-radius:50%;background:var(--ink);top:102px}

  .code-box{position:absolute;left:26px;top:131px;width:101px;height:24px;border:0.8px solid var(--ink);
    display:flex;align-items:center;justify-content:center;font-family:"Montserrat",sans-serif;font-weight:700;font-size:5.8px}
  .distributor{position:absolute;left:26px;top:160.5px;font-size:5.6px;line-height:7.4px;white-space:nowrap}
  .distributor strong{font-family:"Montserrat",sans-serif;font-weight:700}

  .brand-name{position:absolute;left:203px;top:58px;font-family:"Montserrat",sans-serif;font-weight:600;font-size:12.4px;letter-spacing:.3px;white-space:nowrap}
  .product-name{position:absolute;left:200px;top:106px;width:90px;text-align:center;font-family:"Montserrat",sans-serif;font-weight:700;font-size:8.6px;line-height:12.5px;letter-spacing:.6px}
  .organic-seal{position:absolute;left:204px;top:153px;width:25px;height:25px;border-radius:50%;background:var(--organic-green);border:2px solid #fff;box-shadow:0 0 0 0.8px #8a8a8a}
  .potency{position:absolute;left:232px;top:159.5px;width:54px;text-align:right;font-family:"Montserrat",sans-serif;font-weight:500;font-size:5.4px;line-height:7.6px;white-space:nowrap}
  .potency .volume{font-weight:700;letter-spacing:.4px}

  .facts{position:absolute;left:315px;top:22px;width:108px;height:97px;border:0.8px solid var(--ink);font-size:5px}
  .facts > *{position:absolute;left:3px;right:5px}
  .facts-title{top:0.5px;font-family:"Montserrat",sans-serif;font-weight:700;font-size:7.2px}
  .row{display:flex;justify-content:space-between;line-height:5.6px;white-space:nowrap}
  .row .amt{position:absolute;left:58px}
  .rule{height:0;border-top:0.6px solid var(--ink)}
  .rule.thick{border-top-width:1.6px}
  .indent{padding-left:5px}
  .note{line-height:6.3px}

  .ingredients{position:absolute;left:315px;top:123px;font-size:5px;line-height:6.5px;width:100px}
  .follow{position:absolute;left:315px;top:152px;font-size:5px}
  .social-list{position:absolute;right:17px;top:157px;display:flex;align-items:center;gap:5px;list-style:none}
  .social{display:flex;align-items:center;gap:1.5px;white-space:nowrap;font-family:"Montserrat",sans-serif;font-weight:600;font-size:4.8px;line-height:6px}
  .social i{flex:none;display:block;width:5px;height:5px;border-radius:50%;background:var(--ink)}
</style>
</head>
<body>

  <!-- crop marks, upper proof -->
  <div class="crop v" style="left:393px;top:50px;height:52px"></div>
  <div class="crop v" style="left:822px;top:50px;height:52px"></div>
  <div class="crop v" style="left:393px;top:338px;height:51px"></div>
  <div class="crop v" style="left:822px;top:338px;height:51px"></div>
  <div class="crop h" style="left:315px;top:128px;width:52px"></div>
  <div class="crop h" style="left:848px;top:128px;width:52px"></div>
  <div class="crop h" style="left:315px;top:311px;width:52px"></div>
  <div class="crop h" style="left:848px;top:311px;width:52px"></div>

  <!-- crop marks, lower proof -->
  <div class="crop v" style="left:354px;top:420px;height:51px"></div>
  <div class="crop v" style="left:861px;top:420px;height:51px"></div>
  <div class="crop v" style="left:354px;top:745px;height:51px"></div>
  <div class="crop v" style="left:861px;top:745px;height:51px"></div>
  <div class="crop h" style="left:276px;top:497px;width:52px"></div>
  <div class="crop h" style="left:887px;top:497px;width:52px"></div>
  <div class="crop h" style="left:276px;top:718px;width:52px"></div>
  <div class="crop h" style="left:887px;top:718px;width:52px"></div>

  <section class="label label--small">
    <div class="base-band"></div>
    <div class="botanical-strip" role="img" aria-label="Vertical strip of watercolour teal and ink-drawn leafy branches"></div>

    <h2 class="heading suggested-title">SUGGESTED USE</h2>
    <p class="suggested-text">Suggested Use: Take one to two capsules per day or as directed by your physician.</p>
    <p class="warning-text">Warning: consult your healthcare provider if you are nursing, pregnant or taking medication. If adverse reactions occur, discontinue use and consult with your physician. Keep out of reach of children.</p>

    <div class="badge badge--flag" role="img" aria-label="Made in USA badge"></div>
    <div class="badge badge--gluten" role="img" aria-label="Gluten free badge"></div>
    <div class="badge badge--recycle" role="img" aria-label="Recycling badge"></div>

    <div class="code-box">BARCODE HERE</div>
    <p class="distributor"><strong>DISTRIBUTED BY COMPANY NAME</strong><br>Company Address - Website</p>

    <h1 class="brand-name">MOSSLEAF KV</h1>
    <p class="product-name">FULL SPECTRUM<br>HEMP EXTRACT</p>
    <div class="organic-seal" role="img" aria-label="Organic certification seal"></div>
    <p class="potency">less than .3% THC<br><span class="volume">1 fl oz / 30 ml</span></p>

    <div class="facts">
      <div class="facts-title">Supplement Facts</div>
      <div class="row" style="top:10.5px"><span>Serving Size:</span><span>1 dropper (1mL)</span></div>
      <div class="row" style="top:16.5px"><span>Servings Per Container:</span><span>30</span></div>
      <div class="rule thick" style="top:22.5px"></div>
      <div class="row" style="top:25.5px"><span style="padding-left:14px">Amount Per Serving</span><span>%DV*</span></div>
      <div class="rule" style="top:31.5px"></div>
      <div class="row" style="top:33.5px"><span>Calories:</span><span class="amt">10</span></div>
      <div class="rule" style="top:39.5px"></div>
      <div class="row" style="top:41.5px"><span>Total Fat:</span><span class="amt">1g</span><span>2%*</span></div>
      <div class="rule thick" style="top:47.5px"></div>
      <div class="row" style="top:50.5px"><span>Hemp Extract:&nbsp;&nbsp;&nbsp;&nbsp;8.33mg</span><span>†</span></div>
      <div class="row indent" style="top:56.5px"><span>(Leaves &amp; Flowers)</span></div>
      <div class="rule" style="top:62.5px"></div>
      <div class="row indent" style="top:64.5px"><span>CBD:</span><span class="amt">7.5mg</span><span>†</span></div>
      <div class="rule thick" style="top:71px"></div>
      <div class="note" style="top:74.5px">† Daily value not established.<br>**Percent Daily Values (DV) are<br>based on a 2,000 calorie diet.</div>
    </div>

    <p class="ingredients">Active Ingredients: Hemp Extract<br>Inactive Ingredients: MCT Fractionated Coconut Oil.</p>
    <p class="follow">Follow Us</p>
    <ul class="social-list">
      <li class="social"><i></i>Quibblr</li>
      <li class="social"><i></i>Chatterly</li>
      <li class="social"><i></i>Pixaroo</li>
    </ul>

    <div class="safe-area"></div>
  </section>

  <section class="label label--large">
    <div class="base-band"></div>
    <div class="botanical-strip" role="img" aria-label="Vertical strip of watercolour teal and ink-drawn leafy branches"></div>

    <h2 class="heading suggested-title">SUGGESTED USE</h2>
    <p class="suggested-text">Suggested Use: Take one to two capsules per day or as directed by your physician.</p>
    <p class="warning-text">Warning: consult your healthcare provider if you are nursing, pregnant or taking medication. If adverse reactions occur, discontinue use and consult with your physician. Keep out of reach of children.</p>

    <div class="badge badge--flag" role="img" aria-label="Made in USA badge"></div>
    <div class="badge badge--gluten" role="img" aria-label="Gluten free badge"></div>
    <div class="badge badge--recycle" role="img" aria-label="Recycling badge"></div>

    <div class="code-box">BARCODE HERE</div>
    <p class="distributor"><strong>DISTRIBUTED BY COMPANY NAME</strong><br>Company Address - Website</p>

    <h1 class="brand-name">MOSSLEAF KV</h1>
    <p class="product-name">FULL SPECTRUM<br>HEMP EXTRACT</p>
    <div class="organic-seal" role="img" aria-label="Organic certification seal"></div>
    <p class="potency">less than .3% THC<br><span class="volume">1 fl oz / 30 ml</span></p>

    <div class="facts">
      <div class="facts-title">Supplement Facts</div>
      <div class="row" style="top:10.5px"><span>Serving Size:</span><span>1 dropper (1mL)</span></div>
      <div class="row" style="top:16.5px"><span>Servings Per Container:</span><span>30</span></div>
      <div class="rule thick" style="top:22.5px"></div>
      <div class="row" style="top:25.5px"><span style="padding-left:14px">Amount Per Serving</span><span>%DV*</span></div>
      <div class="rule" style="top:31.5px"></div>
      <div class="row" style="top:33.5px"><span>Calories:</span><span class="amt">10</span></div>
      <div class="rule" style="top:39.5px"></div>
      <div class="row" style="top:41.5px"><span>Total Fat:</span><span class="amt">1g</span><span>2%*</span></div>
      <div class="rule thick" style="top:47.5px"></div>
      <div class="row" style="top:50.5px"><span>Hemp Extract:&nbsp;&nbsp;&nbsp;&nbsp;8.33mg</span><span>†</span></div>
      <div class="row indent" style="top:56.5px"><span>(Leaves &amp; Flowers)</span></div>
      <div class="rule" style="top:62.5px"></div>
      <div class="row indent" style="top:64.5px"><span>CBD:</span><span class="amt">7.5mg</span><span>†</span></div>
      <div class="rule thick" style="top:71px"></div>
      <div class="note" style="top:74.5px">† Daily value not established.<br>**Percent Daily Values (DV) are<br>based on a 2,000 calorie diet.</div>
    </div>

    <p class="ingredients">Active Ingredients: Hemp Extract<br>Inactive Ingredients: MCT Fractionated Coconut Oil.</p>
    <p class="follow">Follow Us</p>
    <ul class="social-list">
      <li class="social"><i></i>Quibblr</li>
      <li class="social"><i></i>Chatterly</li>
      <li class="social"><i></i>Pixaroo</li>
    </ul>

    <div class="safe-area"></div>
  </section>

</body>
</html>
```